Make a high end Clubcard for personal training studio. Not a business card but a clubcard

Important! Not a business card buT a clubcard

I need club cards for my clients to check in. My personal training studio is a high end studio with high prices so it needs to look classy and expensive.

You can use the attachment that you like.

the website url needs to be on the card www.Huvelkamp.nl

The card needs to have 2 way design.

I will choose the best Design and have more projects for the winner

Place the following text on the one side of the card:

Personal Training Studio Veldmeer

personal training and fitness

Fitness

53,9 x 85,7mm

• Classy and expensive
• Classy and expensive

```html
<!DOCTYPE html>
<html lang="en">
<head>
<meta charset="utf-8">
<title>Huvelkamp sport – Clubcard</title>
<link rel="stylesheet" href="https://fonts.googleapis.com/css2?family=Roboto+Slab:wght@700;800&family=Merriweather:wght@400&family=Open+Sans:wght@400;600&display=swap">
<style>
  :root {
    --backdrop: #e9e6e1;
    --card-light: #f4f4f4;
    --card-mid: #d9d9d9;
    --card-dark: #bdbdbd;
    --brand-red: #ee3f45;
    --deep-red: #a3121b;
    --ink: #1d1d1d;
    --grey-text: #6f6f6f;
    --big-grey: #9a9a9a;
    --ring: #3a3a3a;
  }
  * { margin: 0; padding: 0; box-sizing: border-box; }
  html, body { width: 1200px; height: 1023px; overflow: hidden; }
  body {
    background: var(--backdrop);
    display: flex;
    flex-direction: column;
    align-items: center;
    justify-content: center;
    gap: 40px;
  }
  .club-card {
    position: relative;
    width: 730px;
    height: 459px;
    border-radius: 10px;
    overflow: hidden;
    background: linear-gradient(135deg, var(--card-light) 0%, var(--card-mid) 55%, var(--card-dark) 100%);
    box-shadow: 0 6px 18px rgba(0,0,0,0.18);
  }
  .card-texture {
    position: absolute; inset: 0;
    background: radial-gradient(ellipse at 35% 30%, rgba(255,255,255,0.55), rgba(255,255,255,0) 65%);
  }
  /* front */
  .brand-mark {
    position: absolute;
    left: 60px; top: 174px;
    width: 112px; height: 112px;
    border-radius: 50%;
    border: 8px solid var(--ring);
    background: #fff;
  }
  .front-title {
    position: absolute;
    left: 200px; top: 160px;
    white-space: nowrap;
  }
  .front-title__brand {
    font-family: "Roboto Slab", serif;
    font-weight: 800;
    font-size: 50px;
    line-height: 1.05;
    color: var(--brand-red);
  }
  .front-title__service {
    font-family: "Roboto Slab", serif;
    font-weight: 800;
    font-size: 44px;
    line-height: 1.15;
    color: var(--ink);
  }
  .front-title__tagline {
    font-family: "Merriweather", serif;
    font-size: 15px;
    letter-spacing: 1px;
    color: var(--ink);
    margin-top: 8px;
  }
  /* back */
  .back-heading {
    position: absolute;
    left: 60px; top: 70px;
    font-family: "Open Sans", sans-serif;
    font-weight: 600;
    font-size: 104px;
    line-height: 1;
    color: var(--big-grey);
  }
  .back-details {
    position: absolute;
    left: 64px; top: 200px;
    font-family: "Open Sans", sans-serif;
    white-space: nowrap;
  }
  .back-details__studio { font-size: 24px; color: var(--grey-text); }
  .back-details__service { font-size: 20px; color: var(--grey-text); margin-top: 4px; }
  .back-details__url { font-size: 22px; color: var(--deep-red); margin-top: 16px; }
  .back-bands { position: absolute; left: 0; bottom: 0; width: 730px; height: 140px; }
</style>
</head>
<body>
  <section class="club-card club-card--front" aria-label="Clubcard front">
    <div class="card-texture" role="img" aria-label="Soft grey faceted background pattern"></div>
    <span class="brand-mark"></span>
    <div class="front-title">
      <p class="front-title__brand">Huvelkamp sport</p>
      <p class="front-title__service">Personal training</p>
      <p class="front-title__tagline">YOUR HEALTH IS OUR CHALLENGE</p>
    </div>
  </section>

  <section class="club-card club-card--back" aria-label="Clubcard back">
    <div class="card-texture" role="img" aria-label="Soft grey faceted background pattern"></div>
    <p class="back-heading">Clubcard</p>
    <div class="back-details">
      <p class="back-details__studio">Personal Training Studio Veldmeer</p>
      <p class="back-details__service">personal training and fitness</p>
      <p class="back-details__url">www.Huvelkamp.nl</p>
    </div>
    <svg class="back-bands" viewBox="0 0 730 140" aria-hidden="true">
      <polygon points="0,140 0,100 730,20 730,140" fill="#c0141e"/>
      <polygon points="0,140 0,118 730,55 730,140" fill="#8e0d15"/>
      <polygon points="260,140 730,80 730,140" fill="#e0262f"/>
    </svg>
  </section>
</body>
</html>
```